Inspiration Poster

Inspirational Poster that has a Kamran Dulo like abstract look (http://www.vexalo.com/images/search?q=kamran+dulo&FORM=HDRSC2) with the text:

"we walk not in order to arrive at the promise land but because walking itself is a revolution"
-Peter Ambrick

```html
<!DOCTYPE html>
<html lang="en">
<head>
<meta charset="utf-8">
<title>Inspiration Poster</title>
<link rel="stylesheet" href="https://fonts.googleapis.com/css2?family=Inter:wght@400;800&display=swap">
<style>
  :root {
    --rust: #b4541f;
    --ember: #d9782f;
    --sky: #3f86c4;
    --violet: #4a3fa0;
    --teal: #2f6d6a;
    --deep: #3a2a22;
    --quote: rgba(255, 255, 255, 0.86);
    --wedge: rgba(255, 255, 255, 0.16);
  }
  html, body {
    margin: 0;
    padding: 0;
    overflow: hidden;
  }
  body {
    width: 1200px;
    height: 801px;
  }
  .poster {
    position: relative;
    width: 1200px;
    height: 801px;
    overflow: hidden;
  }
  .artwork {
    position: absolute;
    inset: 0;
    background:
      radial-gradient(ellipse 420px 180px at 280px 40px, var(--violet) 0%, transparent 70%),
      radial-gradient(ellipse 520px 220px at 850px 60px, var(--sky) 0%, transparent 75%),
      radial-gradient(ellipse 520px 380px at 1030px 560px, var(--teal) 0%, transparent 75%),
      radial-gradient(ellipse 600px 500px at 180px 520px, var(--ember) 0%, transparent 75%),
      linear-gradient(180deg, var(--rust) 0%, #8a4a2a 55%, var(--deep) 100%);
  }
  .light-wedge {
    position: absolute;
    inset: 0;
    width: 1200px;
    height: 801px;
  }
  .light-wedge polygon {
    fill: var(--wedge);
  }
  .quote-block {
    position: absolute;
    left: 20px;
    top: 206px;
    width: 1200px;
    display: flex;
    flex-direction: column;
    align-items: center;
    font-family: "Inter", sans-serif;
    color: var(--quote);
  }
  .quote {
    margin: 0;
    text-align: center;
    font-weight: 800;
    font-size: 80px;
    line-height: 68px;
    letter-spacing: -3.5px;
  }
  .author {
    margin: 8px 0 0;
    text-align: center;
    font-weight: 400;
    font-size: 15px;
    line-height: 18px;
  }
</style>
</head>
<body>
  <main class="poster">
    <div class="artwork" role="img" aria-label="Abstract colour-shifted photograph of tangled orange branches and twigs against blue sky and teal water"></div>
    <svg class="light-wedge" viewBox="0 0 1200 801" aria-hidden="true">
      <polygon points="1200,90 1200,200 300,765"/>
    </svg>
    <div class="quote-block">
      <p class="quote">“we walk not in<br>order to arrive at<br>the promise land<br>but because<br>walking itself is a<br>revolution”</p>
      <p class="author">Peter Ambrick</p>
    </div>
  </main>
</body>
</html>
```